General Dental Office Business Card

I run a private general dental office in southern California, and would like a refresh/redesign of my business card. I focus on quality care rather than volume. The email address on the uploaded current card should be updated to: info@ferncrestvaledental.com. The current card's logo is a deboss, but I am open to other ideas. The logo can be refreshed, but it is something that's been with me since the beginning of the office, so I wouldn't want a drastic redesign.
Target Market(s)
Adults 18-99, whoever needs dental services
Industry/Entity Type
Healthcare/Dental
Contact Information for Business Card
Name, Address, Phone, email
Colors
Designer to choose colors to be used in the design.
Requirements
Must have
- Logo (Same as original one in the uploaded file), space on back for appointment time/date

```html
<!DOCTYPE html>
<html lang="en">
<head>
<meta charset="utf-8">
<title>Ferncrest Vale Dental – Business Card</title>
<link href="https://fonts.googleapis.com/css2?family=Montserrat:wght@400;500;600&display=swap" rel="stylesheet">
<style>
  :root {
    --backdrop: #3b3b3d;
    --card-white: #ffffff;
    --sky: #86d5ec;
    --sky-deep: #7ccfe8;
    --sky-light: #95dcef;
    --ink: #1d1d1f;
    --dots: #555;
  }
  * { box-sizing: border-box; margin: 0; padding: 0; }
  html, body { width: 1200px; height: 1200px; overflow: hidden; }
  body {
    background: var(--backdrop);
    font-family: "Montserrat", sans-serif;
    display: flex;
    flex-direction: column;
    align-items: center;
    justify-content: center;
    gap: 56px;
  }
  .card {
    width: 900px;
    height: 514px;
    border-radius: 40px;
    position: relative;
    overflow: hidden;
  }
  /* Front */
  .card-front { background: var(--card-white); color: var(--ink); }
  .identity { position: absolute; left: 80px; top: 92px; }
  .doctor-name {
    color: var(--sky-deep);
    font-weight: 500;
    font-size: 40px;
    letter-spacing: 0.5px;
    line-height: 1.1;
  }
  .specialty { font-size: 32px; font-weight: 400; margin-top: 2px; }
  .contact-list { list-style: none; margin-top: 26px; }
  .contact-list li {
    display: flex;
    align-items: flex-start;
    gap: 16px;
    font-size: 24px;
    line-height: 1.32;
  }
  .contact-list svg { width: 26px; height: 26px; flex: none; margin-top: 3px; fill: var(--sky-deep); }
  .brand-mark {
    position: absolute;
    right: 70px;
    top: 70px;
    width: 280px;
    display: flex;
    flex-direction: column;
    align-items: center;
    gap: 18px;
  }
  .brand-circle { width: 220px; height: 220px; border-radius: 50%; background: var(--sky); }
  .brand-name-small { color: var(--sky-deep); font-size: 24px; font-weight: 500; white-space: nowrap; }
  .appointment {
    position: absolute;
    left: 80px;
    right: 70px;
    bottom: 52px;
    display: flex;
    gap: 40px;
    font-size: 24px;
  }
  .appointment-field { flex: 1; display: flex; align-items: flex-end; gap: 10px; }
  .appointment-line { flex: 1; border-bottom: 2px dotted var(--dots); margin-bottom: 6px; }
  /* Back */
  .card-back {
    background: linear-gradient(135deg, var(--sky-light), var(--sky-deep));
    display: flex;
    flex-direction: column;
    align-items: center;
    justify-content: center;
    gap: 36px;
  }
  .brand-circle-large { width: 250px; height: 250px; border-radius: 50%; background: var(--card-white); }
  .brand-name-large { color: var(--card-white); font-size: 62px; font-weight: 500; letter-spacing: 1px; }
</style>
</head>
<body>
  <section class="card card-front">
    <div class="identity">
      <h1 class="doctor-name">LAURA M. BRANDT DDS</h1>
      <p class="specialty">General Dentistry</p>
      <ul class="contact-list">
        <li><svg viewBox="0 0 24 24" aria-hidden="true"><path d="M6.6 10.8a15.1 15.1 0 0 0 6.6 6.6l2.2-2.2a1 1 0 0 1 1-.25 11.4 11.4 0 0 0 3.6.57 1 1 0 0 1 1 1V20a1 1 0 0 1-1 1A17 17 0 0 1 3 4a1 1 0 0 1 1-1h3.5a1 1 0 0 1 1 1c0 1.25.2 2.45.57 3.57a1 1 0 0 1-.25 1z"/></svg>949-555-0147</li>
        <li><svg viewBox="0 0 24 24" aria-hidden="true"><path d="M2 5h20v14H2z M3.5 6.5 12 13l8.5-6.5" fill="none" stroke="#7ccfe8" stroke-width="2"/></svg>info@ferncrestvaledental.com</li>
        <li><svg viewBox="0 0 24 24" aria-hidden="true"><g fill="none" stroke="#7ccfe8" stroke-width="1.8"><circle cx="12" cy="12" r="9.5"/><ellipse cx="12" cy="12" rx="4.2" ry="9.5"/><path d="M2.5 12h19M4 7h16M4 17h16"/></g></svg>www.ferncrestvaledental.com</li>
        <li><svg viewBox="0 0 24 24" aria-hidden="true"><path d="M12 2a7 7 0 0 0-7 7c0 5.2 7 13 7 13s7-7.8 7-13a7 7 0 0 0-7-7zm0 9.5A2.5 2.5 0 1 1 12 6.5a2.5 2.5 0 0 1 0 5z"/></svg><span>2150 Alder Glen Parkway<br>Ferncrest, CA 92699</span></li>
      </ul>
    </div>
    <div class="brand-mark">
      <div class="brand-circle"></div>
      <span class="brand-name-small">Ferncrest Vale Dental</span>
    </div>
    <div class="appointment">
      <div class="appointment-field"><span>Date:</span><span class="appointment-line"></span></div>
      <div class="appointment-field"><span>Time:</span><span class="appointment-line"></span></div>
    </div>
  </section>

  <section class="card card-back">
    <div class="brand-circle-large"></div>
    <p class="brand-name-large">Ferncrest Vale Dental</p>
  </section>
</body>
</html>
```